Pig club info pack flyers

We need base artwork to which we can add headings and content. we are looking for double sided A4 designs with blank Word suitable blocks which can hold content on topics including the law, research findings, zoonotic diseases etc etc.
We want them bright but not too complex nor too cartoonish. they object is to be eye-catching but credible. Colours should reflect our logo colours. The running pig line art, if used, should be the yellow in our logo. Maybe a standard heading such as THE FACTS. Open to all ideas.
Target Market(s)
Potential members, existing members, land managers
Industry/Entity Type
Conservation/hunting

```html
<!DOCTYPE html>
<html lang="en">
<head>
<meta charset="utf-8">
<title>Income With Pig's Design Club – Info Pack</title>
<link rel="stylesheet" href="https://fonts.googleapis.com/css2?family=Source+Sans+3:wght@400;600&display=swap">
<style>
:root{
  --backdrop:#4a4a48;
  --paper:#ffffff;
  --ink-dark:#1d2021;
  --gold:#f1a52a;
  --olive:#4f4a2a;
  --text:#5c5c5c;
  --heading:#555759;
  --icon:#6d70a0;
  --rule:#6a6a6a;
}
*{box-sizing:border-box;margin:0;padding:0}
html,body{width:1200px;height:789px;overflow:hidden;background:var(--backdrop)}
body{position:relative;font-family:"Source Sans 3",sans-serif;color:var(--text)}
.page{position:absolute;top:39px;width:501px;height:710px;background:var(--paper);overflow:hidden;box-shadow:0 2px 6px rgba(0,0,0,.35)}
.page--front{left:73px}
.page--back{left:616px}
.abs{position:absolute}
.band-bottom{position:absolute;left:0;bottom:0;width:100%;height:16px;background:linear-gradient(90deg,var(--gold) 0%,#c8902a 55%,var(--olive) 100%)}
.hero-shapes{position:absolute;left:0;top:0}
.title{position:absolute;left:35px;top:52px;font-size:35px;line-height:36.5px;color:#fff;font-weight:400;letter-spacing:.2px}
.brand{position:absolute;left:306px;top:88px;width:162px;display:flex;align-items:center;gap:8px;color:#fff;font-size:15px;line-height:18px;font-weight:400}
.brand-dot{flex:none;width:26px;height:26px;border-radius:50%;background:var(--gold)}
.pig-art{position:absolute;left:180px;top:160px;width:240px;height:120px;background:radial-gradient(ellipse at center,rgba(241,165,42,.16) 0%,rgba(241,165,42,.06) 55%,rgba(241,165,42,0) 72%)}
.block-title{font-size:13px;line-height:15.6px;font-weight:400;color:var(--heading)}
.copy{font-size:8.1px;line-height:10.1px;color:var(--text);overflow:hidden}
.photo{position:absolute;border:1.5px solid #e2e2e2}
.photo--field{background:linear-gradient(180deg,#a9b98a 0%,#6f8a4a 60%,#4e6634 100%)}
.photo--show{background:linear-gradient(180deg,#bcd3e6 0%,#8ea36f 55%,#2b2a2c 100%)}
.photo--class{background:linear-gradient(135deg,#c7cbd0 0%,#9aa1a8 50%,#5d6a78 100%)}
.photo--archive{background:linear-gradient(135deg,#7a4a22 0%,#b07a3c 50%,#1f2535 100%)}
.photo--dinner{background:linear-gradient(135deg,#9a7a4a 0%,#c9a36a 45%,#3a3432 100%);border:2px solid #fff}
.panel{position:absolute;padding:8px 8px}
.panel--dark{background:var(--ink-dark)}
.panel--gold{background:var(--gold)}
.panel .block-title,.panel .copy{color:#fff}
.rule-v{position:absolute;width:1px;background:var(--rule)}
.rule-h{position:absolute;height:1px;background:var(--rule)}
.contact{position:absolute;top:651px;width:100px;text-align:center;font-size:9.5px;line-height:11px;color:var(--text);white-space:nowrap}
.contact-icon{display:block;margin:0 auto 6px;width:20px;height:20px;border-radius:50%;background:var(--icon)}
.contact-icon svg{display:block;width:20px;height:20px}
</style>
</head>
<body>

<section class="page page--front">
  <svg class="hero-shapes" width="501" height="340" viewBox="0 0 501 340">
    <defs>
      <linearGradient id="goldBand" x1="0" y1="0" x2="1" y2="0">
        <stop offset="0" stop-color="#f1a52a"/>
        <stop offset=".6" stop-color="#d49a2c"/>
        <stop offset="1" stop-color="#5a5028"/>
      </linearGradient>
    </defs>
    <polygon points="0,0 501,0 501,214 386,318 0,155" fill="#1d2021"/>
    <polygon points="0,155 386,318 501,214 501,243 386,331 0,187" fill="url(#goldBand)"/>
    <polygon points="300,300 386,331 501,243 501,250 386,340 300,307" fill="#1d2021"/>
  </svg>
  <h1 class="title">INCOME WITH<br>PIG’S DESIGN<br>CLUB</h1>
  <div class="brand"><span class="brand-dot"></span><span>Ridgeline Hunters Society</span></div>
  <div class="pig-art" role="img" aria-label="Running pig line art in gold"></div>

  <h2 class="block-title abs" style="left:35px;top:264px;width:140px">Skills with practical courses and training</h2>
  <p class="copy abs" style="left:35px;top:301px;width:132px;height:213px">How to develop design, motion, and sales skills with practical courses and training, even if you are starting from scratch and investing little time and money; How to make the most of available resources and overcome creative blocks, boosting your growth as a freelancer in the design world; How to use Instagram to attract customers and generate a surprisingly high monthly income of up to $ 5,000 or more. How to develop design, motion, and sales skills with practical courses and training, even if you are starting from scratch and investing little time and money; How to make the most of available resources and overcome creative blocks, boosting your growth as a freelancer in the design world; How to use Instagram to</p>
  <div class="photo photo--show" style="left:35px;top:521px;width:127px;height:116px" role="img" aria-label="Pig show with handlers in white coats"></div>

  <div class="rule-v" style="left:185px;top:321px;height:318px"></div>

  <h2 class="block-title abs" style="left:195px;top:322px;width:125px">Skills with practical courses and training</h2>
  <p class="copy abs" style="left:195px;top:359px;width:262px;height:42px">We need base artwork to which we can add headings and content. we are looking for double sided A4 designs with blank Word suitable blocks which can hold content on topics including the law, research findings, zoonotic diseases etc etc</p>

  <div class="panel panel--dark" style="left:194px;top:413px;width:135px;height:227px">
    <h2 class="block-title">Skills with practical courses and training</h2>
    <div class="photo photo--field" style="left:8px;top:44px;width:114px;height:78px" role="img" aria-label="Two people inspecting a grassy field"></div>
    <p class="copy" style="margin-top:100px;width:118px">We need base artwork to which we can add headings and content. we are looking for double sided A4 designs with blank Word suitable blocks which can hold content on topics including the law, research findings, zoonotic diseases etc etc</p>
  </div>

  <h2 class="block-title abs" style="left:346px;top:411px;width:125px">Skills with practical courses and training</h2>
  <p class="copy abs" style="left:346px;top:447px;width:116px;height:193px">How to develop design, motion, and sales skills with practical courses and training, even if you are starting from scratch and investing little time and money; How to make the most of available resources and overcome creative blocks, boosting your growth as a freelancer in the design world; How to use Instagram to attract customers and generate a surprisingly high monthly income of up to $ 5,000 or more. How to develop design, motion, and sales skills with practical courses and training, even if you are starting from scratch and investing little time and money;</p>

  <div class="contact" style="left:99px">
    <span class="contact-icon"><svg viewBox="0 0 20 20"><g fill="none" stroke="#fff" stroke-width="1"><circle cx="10" cy="10" r="6"/><ellipse cx="10" cy="10" rx="2.6" ry="6"/><line x1="4" y1="10" x2="16" y2="10"/><line x1="5" y1="7" x2="15" y2="7"/><line x1="5" y1="13" x2="15" y2="13"/></g></svg></span>
    www.ridgeline.org
  </div>
  <div class="contact" style="left:204px">
    <span class="contact-icon"><svg viewBox="0 0 20 20"><g fill="none" stroke="#fff" stroke-width="1"><rect x="4.5" y="6.5" width="11" height="7.5"/><polyline points="4.5,6.5 10,11 15.5,6.5"/></g></svg></span>
    info@ridgeline.org
  </div>
  <div class="contact" style="left:307px">
    <span class="contact-icon"><svg viewBox="0 0 20 20"><path d="M7 4.5l2 3-1.3 1.3a7 7 0 0 0 3.5 3.5L12.5 11l3 2-1.2 2.2c-5 .2-9.8-4.6-9.5-9.5z" fill="#fff"/></svg></span>
    (000)555-210-734
  </div>
  <div class="band-bottom"></div>
</section>

<section class="page page--back">
  <h2 class="block-title abs" style="left:29px;top:40px;width:130px">Skills with practical courses and training</h2>
  <p class="copy abs" style="left:29px;top:78px;width:132px;height:243px">How to develop design, motion, and sales skills with practical courses and training, even if you are starting from scratch and investing little time and money; How to make the most of available resources and overcome creative blocks, boosting your growth as a freelancer in the design world; How to use Instagram to attract customers and generate a surprisingly high monthly income of up to $ 5,000 or more. How to develop design, motion, and sales skills with practical courses and training, even if you are starting from scratch and investing little time and money; How to make the most of available resources and overcome creative blocks, boosting your growth as a freelancer in the design world; How to use Instagram to attract customers and generate a surprisingly high monthly income of up to $ 5,000 or more.</p>
  <div class="photo photo--archive" style="left:29px;top:334px;width:131px;height:130px" role="img" aria-label="Two people examining items in a display case"></div>

  <div class="rule-v" style="left:178px;top:41px;height:422px"></div>

  <h2 class="block-title abs" style="left:194px;top:38px;width:270px">Skills with practical courses and training</h2>
  <p class="copy abs" style="left:194px;top:56px;width:262px;height:21px">How to develop design, motion, and sales skills with practical courses and training, even if you are starting from scratch and investing little time and</p>
  <div class="photo photo--class" style="left:193px;top:83px;width:122px;height:122px" role="img" aria-label="Students talking in a library"></div>
  <p class="copy abs" style="left:320px;top:77px;width:134px;height:132px">money; How to make the most of available resources and overcome creative blocks, boosting your growth as a freelancer in the design world; How to use Instagram to attract customers and generate a surprisingly high monthly income of up to $ 5,000 or more. How to develop design, motion, and sales skills with practical courses and training, even if you are starting from scratch and investing little time and money; How to make the most of</p>

  <div class="rule-h" style="left:190px;top:221px;width:282px"></div>

  <div class="panel panel--gold" style="left:193px;top:234px;width:135px;height:227px">
    <h2 class="block-title">Skills with practical courses and training</h2>
    <div class="photo photo--field" style="left:8px;top:45px;width:114px;height:78px" role="img" aria-label="Two people inspecting a grassy field"></div>
    <p class="copy" style="margin-top:99px;width:118px">We need base artwork to which we can add headings and content. we are looking for double sided A4 designs with blank Word suitable blocks which can hold content on topics including the law, research findings, zoonotic diseases etc etc</p>
  </div>

  <h2 class="block-title abs" style="left:346px;top:233px;width:125px">Skills with practical courses and training</h2>
  <p class="copy abs" style="left:346px;top:269px;width:120px;height:192px">How to develop design, motion, and sales skills with practical courses and training, even if you are starting from scratch and investing little time and money; How to make the most of available resources and overcome creative blocks, boosting your growth as a freelancer in the design world; How to use Instagram to attract customers and generate a surprisingly high monthly income of up to $ 5,000 or more. How to develop design, motion, and sales skills with practical courses and training, even if you are starting from scratch and investing little time and money;</p>

  <div class="panel panel--dark" style="left:29px;top:482px;width:443px;height:197px;padding:17px 8px">
    <h2 class="block-title" style="width:112px">You are family, you make a difference.</h2>
    <p class="copy" style="margin-top:10px;width:180px;height:132px">How to develop design, motion, and sales skills with practical courses and training, even if you are starting from scratch and investing little time and money; How to make the most of available resources and overcome creative blocks, boosting your growth as a freelancer in the design world; How to use Instagram to attract customers and generate a surprisingly high monthly income of up to $ 5,000 or more. How to develop design, motion, and sales skills with practical courses and training, even if you are starting from scratch and investing little time and money; How to make the most of available resources and overcome creative</p>
    <div class="photo photo--dinner" style="left:205px;top:18px;width:222px;height:164px" role="img" aria-label="Guests holding plates at a community dinner"></div>
  </div>
  <div class="band-bottom"></div>
</section>

</body>
</html>
```